Custom t-shirts and merchandise orders t shirts and merchendise

I'd like to build a webpage to promote clothing apparel merchandise and also print on demand. A copy of my logo is attached! An example webpage for the print on demand would be pembrotees.com, Quillmarktees.com, and vexaprinting.com. If possible, I'd like the web page colors to match the attached logo but it is not absolutely necessary.

Target Market(s)

Viddora, Chatterly, and zindex viewers age 20-35

Industry/Entity Type

Apparel Store

Logo Text

RimDunes

Coding

Coded - Design and coding required

Number of Pages Required

5+ page

Font styles to use
Sans Serif

Requirements
Must have
• Print on demand page to custom build a shirt design.
Nice to have
• Subscribe option

```html
<!DOCTYPE html>
<html lang="en">
<head>
<meta charset="utf-8">
<title>InkHarbor – Custom Shirts</title>
<link href="https://fonts.googleapis.com/css2?family=Poppins:wght@400;600;700&family=Roboto:wght@400;500;700&display=swap" rel="stylesheet">
<style>
:root{
  --blue:#00aeef;
  --blue-line:#29a8e0;
  --pink:#e6007e;
  --ink:#111;
  --text:#333;
  --muted:#777;
  --bar:#f4f4f4;
  --soft:#f3f3f3;
  --card-line:#e2e2e2;
  --footer:#2a2a2a;
  --footer-line:#3c3c3c;
  --green:#3cb371;
}
*{box-sizing:border-box;margin:0;padding:0}
html,body{width:1200px;height:3456px;overflow:hidden;background:#fff}
body{position:relative;font-family:"Roboto",sans-serif;color:var(--text)}
.abs{position:absolute}
h2.section-title{position:absolute;left:0;width:1200px;text-align:center;font-family:"Poppins",sans-serif;font-size:38px;font-weight:400;color:var(--ink)}
h2.section-title b{font-weight:700}

/* top bar */
.top-bar{left:0;top:0;width:1200px;height:44px;background:var(--bar);border-bottom:1px solid #e6e6e6}
.top-bar .claim{left:0;width:1200px;top:13px;text-align:center;font-size:14px;color:#666}
.top-bar .account{left:860px;top:13px;font-size:14px;font-weight:500;color:#222;display:flex;align-items:center;gap:6px}
.top-bar .cart{left:985px;top:7px;width:101px;height:30px;border:2px solid #ccc;border-radius:15px;font-size:14px;font-weight:500;color:#222;display:flex;align-items:center;padding-left:11px;gap:6px}
.cart .count{margin-left:auto;margin-right:6px;background:#bbb;border-radius:9px;width:22px;height:18px;text-align:center;font-size:12px;line-height:18px}

/* header */
.main-nav{left:111px;top:76px;display:flex;gap:16px;font-size:15px;font-weight:500;color:#111}
.main-nav span{color:#111}
.logo-plate{left:470px;top:128px;width:260px;height:50px;background:#fff;clip-path:polygon(0 0,100% 0,88% 100%,12% 100%)}
.logo{left:500px;top:118px;width:200px;text-align:center;font-family:"Poppins",sans-serif;font-size:34px;font-weight:700;color:var(--ink);display:flex;justify-content:center;align-items:center;gap:8px}
.logo .dot{width:14px;height:14px;border-radius:50%;background:var(--pink)}
.help{top:66px;display:flex;gap:10px;align-items:center}
.help .big{font-size:16px;color:var(--blue);font-weight:500}
.help .small{font-size:12px;color:#555}
.help .small::before{content:"";display:inline-block;width:5px;height:5px;border-radius:50%;background:var(--green);margin-right:5px;vertical-align:middle}

/* hero */
.hero-blue{left:0;top:130px;width:1200px;height:575px;background:var(--blue)}
.hero-photo{left:0;top:130px;width:1200px;height:575px;
  background:
    radial-gradient(ellipse 330px 140px at 860px 440px,rgba(140,190,225,.95),rgba(140,190,225,0) 100%),
    radial-gradient(ellipse 200px 110px at 1110px 450px,rgba(140,190,225,.9),rgba(140,190,225,0) 100%),
    radial-gradient(ellipse 260px 120px at 860px 650px,rgba(52,78,120,.95),rgba(52,78,120,0) 100%),
    radial-gradient(ellipse 150px 110px at 820px 300px,rgba(214,170,140,.7),rgba(214,170,140,0) 100%),
    radial-gradient(ellipse 180px 120px at 1020px 330px,rgba(222,180,145,.6),rgba(222,180,145,0) 100%),
    linear-gradient(180deg,#3f5730 0%,#5d7a45 30%,#7e9a62 45%,#86a9c9 65%,#5d7fa8 85%,#3e5a86 100%);
  clip-path:polygon(490px 0,1200px 0,1200px 575px,592px 575px)}
.hero-copy{left:111px;top:320px;color:#fff}
.hero-copy h1{font-family:"Poppins",sans-serif;font-size:44px;font-weight:600;line-height:1}
.hero-copy p{margin-top:24px;font-size:17px;font-weight:500;line-height:25px;width:360px}
.btn{display:flex;align-items:center;justify-content:center;gap:8px;background:var(--pink);color:#fff;font-weight:700;font-size:16px;border-radius:24px;text-transform:uppercase}
.hero-btn{left:111px;top:458px;width:227px;height:47px}

/* categories */
.cat-card{width:223px;height:264px;border:1px solid var(--card-line);background:#fff}
.cat-card.active{border:2px solid var(--blue-line);background:#f0faff}
.cat-card .shirt{position:absolute;left:36px;top:22px;width:150px;height:172px;border-radius:18px}
.shirt.dark{background:radial-gradient(ellipse 40px 34px at 50% 48%,#4a4a4a,#1f1f1f 100%),#1c1c1c}
.shirt.grey{background:radial-gradient(ellipse 40px 34px at 50% 48%,#c8c8c8,#8f8f8f 100%),#999}
.cat-card .label{position:absolute;left:0;width:100%;top:220px;text-align:center;font-size:17px;font-weight:500;color:#111}
.shop-all{left:486px;top:1487px;width:228px;height:45px;font-size:15px}

/* features */
.feature{width:262px;height:242px;text-align:center}
.feature.raised{background:#fff;box-shadow:0 0 12px rgba(0,0,0,.1);border:1px solid #eee}
.feature svg{position:absolute;left:106px;top:45px}
.feature h3{position:absolute;left:0;width:100%;top:114px;font-size:19px;font-weight:500;color:#111}
.feature p{position:absolute;left:-10px;width:calc(100% + 20px);top:153px;font-size:14.5px;line-height:23px;color:var(--muted)}

/* testimonials */
.testimonials{left:0;top:2024px;width:1200px;height:496px;background:var(--soft)}
.quote{width:310px;height:190px;background:#fff;border-top:3px solid var(--blue-line);border-radius:14px;box-shadow:0 3px 10px rgba(0,0,0,.08)}
.quote p{position:absolute;left:26px;right:26px;top:65px;text-align:center;font-size:14.5px;line-height:26px;color:#555}
.avatar{width:92px;height:92px;border-radius:50%;border:4px solid #fff;box-shadow:0 0 0 1px #ddd}
.person{width:310px;text-align:center;font-size:15px;font-weight:500;color:#222}
.person small{font-size:10px;font-weight:400}
.stars{display:flex;justify-content:center;gap:2px;margin-top:6px}

/* footer */
.site-footer{left:0;top:3135px;width:1200px;height:321px;background:var(--footer)}
.f-col{top:3203px;color:#fff}
.f-col h4{font-size:17px;font-weight:500;letter-spacing:.2px;margin-bottom:12px;text-transform:uppercase}
.f-col ul{list-style:none;font-size:12px;line-height:22.5px}
.f-div{top:3205px;width:1px;height:150px;background:var(--footer-line)}
.contact li{display:flex;gap:12px;align-items:flex-start;margin-bottom:7px;line-height:16px}
.social li{display:flex;align-items:center;gap:12px;margin-bottom:6px}
.social .circ{width:28px;height:28px;border-radius:50%;background:var(--blue)}
.copyright{left:0;width:1200px;top:3419px;text-align:center;font-size:11px;color:#fff}
</style>
</head>
<body>

<div class="abs top-bar">
  <div class="abs claim">500,000+ Customers Nationwide w/ 99.7% Satisfaction</div>
  <div class="abs account">
    <svg width="14" height="14" viewBox="0 0 14 14"><circle cx="7" cy="7" r="6.5" fill="#222"/><circle cx="7" cy="5.3" r="2.3" fill="#fff"/><path d="M3 11.2c1-2 2.3-2.6 4-2.6s3 .6 4 2.6" fill="#fff"/></svg>
    My Account
  </div>
  <div class="abs cart">
    <svg width="14" height="12" viewBox="0 0 14 12"><path d="M0 1h2.5l2 7h7l2-5.5H3.5" fill="none" stroke="#222" stroke-width="1.6"/><circle cx="5.5" cy="10.5" r="1.2" fill="#222"/><circle cx="10.5" cy="10.5" r="1.2" fill="#222"/></svg>
    Cart <span class="count">0</span>
  </div>
</div>

<nav class="abs main-nav"><span>Custom Shirts</span><span>Brands</span><span>Styles</span><span>Design Services</span></nav>

<div class="abs help" style="left:732px">
  <svg width="34" height="34" viewBox="0 0 34 34" fill="none" stroke="#e6007e" stroke-width="1.8"><path d="M7 19v-3a10 10 0 0 1 20 0v3"/><rect x="4" y="17" width="5" height="8" rx="2"/><rect x="25" y="17" width="5" height="8" rx="2"/><circle cx="17" cy="18" r="5"/></svg>
  <div><div class="big">Live Chat Now</div><div class="small">Chat with an Expert</div></div>
</div>
<div class="abs help" style="left:930px">
  <svg width="34" height="34" viewBox="0 0 34 34" fill="none" stroke="#e6007e" stroke-width="1.8"><circle cx="17" cy="12" r="6"/><path d="M6 31c1-7 5-10 11-10s10 3 11 10"/><path d="M10 13a7 7 0 0 1 14 0"/></svg>
  <div><div class="big">(800) 555-0142</div><div class="small">Talk to an Expert</div></div>
</div>

<div class="abs hero-blue"></div>
<div class="abs hero-photo" role="img" aria-label="Photo of a smiling group of friends outdoors wearing matching light blue custom printed t-shirts"></div>
<div class="abs logo-plate"></div>
<div class="abs" style="left:500px;top:44px;width:200px;height:90px;background:#fff"></div>
<div class="abs logo"><span class="dot"></span>InkHarbor</div>

<div class="abs hero-copy">
  <h1>InkHarbor</h1>
  <p>Lorem ipsum dolor sit amet, consectetur elit, sed do eiusmod tempor incididunt</p>
</div>
<div class="abs btn hero-btn">Start Designing
  <svg width="16" height="16" viewBox="0 0 16 16"><circle cx="8" cy="8" r="7.5" fill="#fff"/><path d="M6.5 4.5 10 8l-3.5 3.5" fill="none" stroke="#e6007e" stroke-width="2"/></svg>
</div>

<h2 class="section-title" style="top:785px"><b>Shop Our Top</b> Categories</h2>

<div class="abs cat-card" style="left:118px;top:885px"><div class="shirt grey" role="img" aria-label="Grey basic t-shirt mockup with sample print"></div><div class="label">Basic Tees</div></div>
<div class="abs cat-card active" style="left:368px;top:885px"><div class="shirt dark" role="img" aria-label="Black brand t-shirt mockup with sample print"></div><div class="label">Brand Tees</div></div>
<div class="abs cat-card" style="left:616px;top:885px"><div class="shirt dark" role="img" aria-label="Black long sleeve shirt mockup with sample print"></div><div class="label">Long Sleeves</div></div>
<div class="abs cat-card" style="left:866px;top:885px"><div class="shirt dark" role="img" aria-label="Black ladies t-shirt mockup with sample print"></div><div class="label">Ladies Tees</div></div>

<div class="abs cat-card" style="left:118px;top:1174px"><div class="shirt dark" role="img" aria-label="Black hoodie mockup with sample print"></div><div class="label">Hoodies</div></div>
<div class="abs cat-card" style="left:368px;top:1174px"><div class="shirt grey" role="img" aria-label="Grey sweatshirt mockup with sample print"></div><div class="label">Sweatshirts</div></div>
<div class="abs cat-card" style="left:616px;top:1174px"><div class="shirt dark" role="img" aria-label="Black tank top mockup with sample print"></div><div class="label">Tanks</div></div>
<div class="abs cat-card" style="left:866px;top:1174px"><div class="shirt dark" role="img" aria-label="Black v-neck t-shirt mockup with sample print"></div><div class="label">V-Necks</div></div>

<div class="abs btn shop-all">Shop All Products
  <svg width="14" height="14" viewBox="0 0 16 16"><circle cx="8" cy="8" r="7.5" fill="#fff"/><path d="M6.5 4.5 10 8l-3.5 3.5" fill="none" stroke="#e6007e" stroke-width="2"/></svg>
</div>

<h2 class="section-title" style="top:1604px"><b>Your Brand Deserves</b> the Best</h2>

<div class="abs feature" style="left:146px;top:1685px">
  <svg width="50" height="44" viewBox="0 0 50 44" fill="none" stroke="#1d8fd6" stroke-width="1.6"><rect x="2" y="10" width="30" height="22"/><path d="M32 17h9l6 7v8H32"/><circle cx="11" cy="35" r="4"/><circle cx="39" cy="35" r="4"/><path d="M12 10c-4-7 5-8 5 0 0-8 9-7 5 0"/><text x="6" y="25" font-size="9" font-family="Roboto,sans-serif" fill="#e6007e" stroke="none" font-weight="700">FREE</text></svg>
  <h3>Rush Shipping</h3>
  <p>Lorem ipsum dolor sit amet, consectetur adipiscing elit, sed do eiusmod</p>
</div>
<div class="abs feature raised" style="left:469px;top:1685px">
  <svg width="50" height="44" viewBox="0 0 50 44" fill="none" stroke="#1d8fd6" stroke-width="1.6"><circle cx="25" cy="14" r="11" stroke="#e6007e"/><path d="M20 19l10-10" stroke="#e6007e"/><circle cx="21" cy="11" r="1.5" stroke="#e6007e"/><circle cx="29" cy="17" r="1.5" stroke="#e6007e"/><path d="M3 32h8l8 3h10c3 0 3 4 0 4H18M11 30l14-3 16-5c3-1 5 2 2 4L28 40H3"/></svg>
  <h3>Better Pricing</h3>
  <p>Lorem ipsum dolor sit amet, consectetur adipiscing elit, sed do</p>
</div>
<div class="abs feature" style="left:792px;top:1685px">
  <svg width="50" height="44" viewBox="0 0 50 44" fill="none" stroke="#1d8fd6" stroke-width="1.6"><rect x="4" y="4" width="42" height="36"/><path d="M10 36V8l28 28z"/><path d="M16 30v-8l8 8z" stroke="#e6007e"/><path d="M28 6l10 16" stroke="#e6007e"/></svg>
  <h3>Design Review &amp; Repair</h3>
  <p>Lorem ipsum dolor sit amet, consectetur adipiscing elit, sed do eiusmod</p>
</div>

<div class="abs testimonials"></div>
<h2 class="section-title" style="top:2068px"><b>What Our</b> Clients Say</h2>

<div class="abs quote" style="left:111px;top:2198px"><p>Sed ut perspiciatis unde omnis iste natus error sit voluptatem accusantium doloremque laudantium, totam rem aperiam, eaque ipsa</p></div>
<div class="abs quote" style="left:445px;top:2198px"><p>Sed ut perspiciatis unde omnis iste natus error sit voluptatem accusantium doloremque laudantium, totam rem aperiam, eaque ipsa</p></div>
<div class="abs quote" style="left:779px;top:2198px"><p>Sed ut perspiciatis unde omnis iste natus error sit voluptatem accusantium doloremque laudantium, totam rem aperiam, eaque ipsa</p></div>

<div class="abs avatar" style="left:220px;top:2154px;background:radial-gradient(circle at 50% 40%,#d9b59a,#8a6a55 60%,#3b3f49 100%)" role="img" aria-label="Client portrait"></div>
<div class="abs avatar" style="left:554px;top:2154px;background:radial-gradient(circle at 50% 40%,#e4c2a8,#3a2a26 60%,#1d1d1f 100%)" role="img" aria-label="Client portrait"></div>
<div class="abs avatar" style="left:888px;top:2154px;background:radial-gradient(circle at 50% 40%,#d8b398,#6d5547 60%,#2b3550 100%)" role="img" aria-label="Client portrait"></div>

<div class="abs person" style="left:111px;top:2413px">Dana Whitfield, <small>Chairman NRC</small>
  <div class="stars"><svg width="68" height="12" viewBox="0 0 68 12"><g fill="#f5c000"><path id="st" d="M6 0l1.8 3.8 4.2.5-3.1 2.9.8 4.1L6 9.3 2.3 11.3l.8-4.1L0 4.3l4.2-.5z"/><use href="#st" x="14"/><use href="#st" x="28"/><use href="#st" x="42"/><use href="#st" x="56"/></g></svg></div>
</div>
<div class="abs person" style="left:445px;top:2413px">Lena Ortiz, <small>Project Manager</small>
  <div class="stars"><svg width="68" height="12" viewBox="0 0 68 12"><g fill="#f5c000"><use href="#st"/><use href="#st" x="14"/><use href="#st" x="28"/><use href="#st" x="42"/><use href="#st" x="56"/></g></svg></div>
</div>
<div class="abs person" style="left:779px;top:2413px">Marcus Hale, <small>Chairman NRC</small>
  <div class="stars"><svg width="68" height="12" viewBox="0 0 68 12"><g fill="#f5c000"><use href="#st"/><use href="#st" x="14"/><use href="#st" x="28"/><use href="#st" x="42"/><use href="#st" x="56"/></g></svg></div>
</div>

<h2 class="section-title" style="top:2585px"><b>See Our</b> Work</h2>
<div class="abs" style="left:198px;top:2667px;width:367px;height:353px;background:radial-gradient(ellipse 220px 90px at 50% 62%,#c4c4c0,rgba(196,196,192,0) 100%),linear-gradient(180deg,#6f7a5c 0%,#8f9480 28%,#b5b5b0 55%,#a2a29c 78%,#566a8c 100%)" role="img" aria-label="Group of volunteers in grey printed t-shirts"></div>
<div class="abs" style="left:578px;top:2667px;width:206px;height:171px;background:linear-gradient(180deg,#a7c08e 0%,#5f8f4d 40%,#2f6b3a 65%,#4f8a3a 100%)" role="img" aria-label="Volunteer team in green shirts outdoors"></div>
<div class="abs" style="left:796px;top:2667px;width:206px;height:171px;background:linear-gradient(180deg,#b9b4ac 0%,#d6d2cb 35%,#f2f1ee 65%,#e4e2de 100%)" role="img" aria-label="Volunteers in white printed t-shirts"></div>
<div class="abs" style="left:578px;top:2850px;width:206px;height:170px;background:linear-gradient(180deg,#d5d8da 0%,#a9b6c2 35%,#7fb0d6 65%,#6a9ec8 100%)" role="img" aria-label="Friends in light blue volunteer t-shirts"></div>
<div class="abs" style="left:796px;top:2850px;width:206px;height:170px;background:linear-gradient(180deg,#9fb07f 0%,#7d9468 35%,#9fb2c8 60%,#6f8f55 100%)" role="img" aria-label="Volunteers planting trees in a park"></div>

<footer class="abs site-footer"></footer>
<div class="abs f-div" style="left:272px"></div>
<div class="abs f-div" style="left:537px"></div>
<div class="abs f-div" style="left:876px"></div>

<div class="abs f-col" style="left:113px">
  <h4>Quick Links</h4>
  <ul><li>Home</li><li>About</li><li>Products</li><li>Shop now</li><li>Sign in</li></ul>
</div>
<div class="abs f-col" style="left:349px">
  <h4>Information</h4>
  <ul><li>Terms &amp; Conditions</li><li>Privacy Policy</li><li>Disclaimer</li><li>Site Map</li><li>Contact Us</li><li>Categories</li></ul>
</div>
<div class="abs f-col" style="left:614px">
  <h4>Contact Info</h4>
  <ul class="contact">
    <li><svg width="14" height="12" viewBox="0 0 14 12"><path d="M1 4c0-3 12-3 12 0v1h-3V4H4v1H1z M3 6h8l1 5H2z" fill="#fff"/></svg>(215) 555-0187</li>
    <li><svg width="14" height="12" viewBox="0 0 14 12"><rect x="3" y="0" width="8" height="4" fill="#fff"/><rect x="1" y="4" width="12" height="5" fill="#fff"/><rect x="3" y="8" width="8" height="4" fill="#fff"/></svg>(215) 555-0187</li>
    <li><svg width="14" height="12" viewBox="0 0 14 12"><rect x="0" y="1" width="14" height="10" fill="#fff"/><path d="M0 1l7 5 7-5" fill="none" stroke="#2a2a2a"/></svg><u>hello@inkharbor.example</u></li>
    <li><svg width="14" height="14" viewBox="0 0 14 14"><path d="M7 0a5 5 0 0 1 5 5c0 4-5 9-5 9S2 9 2 5a5 5 0 0 1 5-5z" fill="#fff"/><circle cx="7" cy="5" r="2" fill="#2a2a2a"/></svg><span>#2868 Lorem ipsum dolor sit<br>amet, consectetur</span></li>
  </ul>
</div>
<div class="abs f-col" style="left:953px">
  <h4>Follow Us</h4>
  <ul class="social">
    <li><span class="circ"></span>Chatterly</li>
    <li><span class="circ"></span>Chirpline</li>
    <li><span class="circ"></span>zindex Plus</li>
    <li><span class="circ"></span>Workbridge</li>
  </ul>
</div>
<div class="abs copyright">Copyrights © InkHarbor Apparel 2021 | Allrights Reserved</div>

</body>
</html>
```